Using Existing Logo to Create Stationary, Powerpoint and Word Background Identity

I am seeking an identity design which can be used in corporate literature and documents which extends the use of our new identity within the company logo. I need to specifically have designed background identity for a stationary set which includes a) A4 Front/Title Page (Portrait and Landscape for Proposals (Word) and Powerpoints (PPT)) b) A4 Content Pages (Same as above) c) A4 Letter Template for Letters (Word) d) Business Cards e) A5 With Compliments Slips. It is critical that the road is used in the identity sets and that content pages have clear text space in all instances.

Please read messages, as I am only seeking artwork and example placement of text in a format I can edit using photoshop. Therefore a business card would be layed out per normal with:
Name:
Company:
Mobile:
Phone:
Email:
Fax:
Address:
Web:
etc.

and stationary would have same except name removed. I have increased the budget to $260AU which has not been shown yet??
Updates

I am hoping someone can come up with a unique branding and identity using the road which can translate across business cards, proposals, presentations etc. I have seen previous work by other quality designers in this area that takes a standard logo image and creates an identity across communications documents and stationary. This is what I seek to achieve. If the identity is created for cards and proposals etc then blanks of each template can be provided as PDF, JPG and editable format (photoshop preferred) which we will alter to allow publishing to take place. Thanks

Can we fit the following on the backside of the card.

- Automating Chain of Responsibility
- Simplifying QBRTE & Velmorix
- Providing Eco-Driving & KLAP Reporting
- Protecting Transport Company Executives

Please change the back of card to these:
- Paperless QBRTE & Velmorix
- Electronic Work Diaries, Safe Driving Plans

All,

A great effort and very hard to determine who gets the gig. Each designer brings a unique flavour to this task. I have eliminated all designs that I do not consider meet the brief (per my opinion).

I will work through with those designers to elaborate the design (where needed) to finalise a design concept, which can then be closed and paid.

Please be patient, and I will be in touch shortly.

Marisol

Thanking all designers for their terrific input. We will announce shortly the design concept we are moving forward with. It has taken much deliberation and was difficult to agree upon.

Target Market(s)

Corporate Transport Customers, Government Departments

Industry/Entity Type

Business

Requirements
Must have
• Must use the existing logo imagery to consolidate into a professional identity set.
Nice to have
• Use of Road in design formats

```html
<!DOCTYPE html>
<html lang="en">
<head>
<meta charset="utf-8">
<title>Veyrant Stationery Identity</title>
<link href="https://fonts.googleapis.com/css2?family=Open+Sans:wght@400;600;800&display=swap" rel="stylesheet">
<style>
  :root {
    --stage: #3b3b3b;
    --margin: #ffffff;
    --paper: #ffffff;
    --brand-green: #4fae2e;
    --brand-blue: #1f4f9e;
    --text-blue: #2a4f98;
    --road-lilac: #dcdfee;
    --road-sage: #e6eedb;
    --muted: #6b7590;
  }
  * { box-sizing: border-box; margin: 0; padding: 0; }
  html, body { width: 1200px; height: 696px; overflow: hidden; background: var(--margin); }
  body { font-family: "Open Sans", Arial, sans-serif; position: relative; }
  .stage { position: absolute; left: 0; top: 0; width: 1074px; height: 696px; background: var(--stage); }
  .sheet { position: absolute; background: var(--paper); overflow: hidden; }

  .road-area {
    position: absolute; left: 0;
    background: linear-gradient(160deg, var(--road-lilac) 0%, var(--road-sage) 60%, rgba(255,255,255,0) 100%);
  }

  .bar { position: absolute; height: 8px; background: var(--brand-green); }
  .bar.top { top: 0; left: 0; }
  .bar.bottom { bottom: 0; right: 0; }

  .wordmark { position: absolute; display: flex; align-items: center; gap: 6px;
    color: var(--brand-blue); font-weight: 800; letter-spacing: -0.5px; white-space: nowrap; line-height: 1; }
  .wordmark .dot { border-radius: 50%; background: var(--brand-green); flex: none; }

  /* Portrait */
  .portrait { left: 40px; top: 40px; width: 422px; height: 600px; }
  .portrait .bar.top { width: 240px; }
  .portrait .bar.bottom { width: 212px; }
  .portrait .title { position: absolute; top: 36px; width: 100%; text-align: center;
    color: var(--text-blue); font-size: 13px; font-weight: 400; }
  .portrait .road-area { top: 440px; width: 250px; height: 160px; }
  .portrait .wordmark { right: 16px; bottom: 26px; font-size: 30px; }
  .portrait .wordmark .dot { width: 14px; height: 14px; }

  /* Landscape */
  .landscape { left: 498px; top: 100px; width: 512px; height: 384px; }
  .landscape .bar.top { width: 242px; }
  .landscape .bar.bottom { width: 220px; height: 6px; }
  .landscape .road-area { top: 240px; width: 300px; height: 144px; }
  .bullets { position: absolute; left: 96px; top: 70px; list-style: none; }
  .bullets li { display: flex; align-items: center; gap: 6px; height: 37px;
    color: var(--text-blue); font-size: 9.5px; white-space: nowrap; }
  .bullets li::before { content: ""; width: 8px; height: 8px; border-radius: 50%; background: var(--brand-blue); flex: none; }
  .landscape .wordmark { right: 14px; bottom: 22px; font-size: 28px; }
  .landscape .wordmark .dot { width: 13px; height: 13px; }

  /* Cards */
  .card { top: 550px; height: 106px; }
  .card .bar { height: 4px; }
  .card-back { left: 594px; width: 182px; }
  .card-back .bar.top { width: 96px; }
  .card-back .bar.bottom { width: 60px; }
  .card-back .road-area { top: 62px; width: 90px; height: 44px; }
  .services { position: absolute; left: 76px; top: 14px; list-style: none;
    color: var(--muted); font-size: 5.5px; line-height: 10px; }
  .services li::before { content: "- "; }
  .card-back .wordmark { right: 8px; bottom: 9px; font-size: 15px; gap: 3px; }
  .card-back .wordmark .dot { width: 6px; height: 6px; }

  .card-front { left: 792px; width: 180px; }
  .card-front .bar.bottom { width: 120px; }
  .card-front .wordmark { left: 6px; top: 7px; font-size: 15px; gap: 3px; }
  .card-front .wordmark .dot { width: 6px; height: 6px; }
  .contact { position: absolute; left: 8px; top: 40px; color: var(--text-blue);
    font-size: 5.5px; line-height: 8px; }
  .contact .name { font-weight: 600; }
  .web { position: absolute; left: 8px; bottom: 10px; color: var(--text-blue); font-size: 5.5px; }
</style>
</head>
<body>
<div class="stage"></div>

<section class="sheet portrait">
  <div class="bar top"></div>
  <h1 class="title">Portrait and Landscape for Proposals</h1>
  <div class="road-area" role="img" aria-label="Soft winding road graphic in lilac and sage"></div>
  <div class="wordmark"><span class="dot"></span>Veyrant</div>
  <div class="bar bottom"></div>
</section>

<section class="sheet landscape">
  <div class="bar top"></div>
  <div class="road-area" role="img" aria-label="Soft winding road graphic in lilac and sage"></div>
  <ul class="bullets">
    <li>Lorem Ipsum is simply dummy text of the printing and typesetting industry</li>
    <li>Lorem Ipsum is simply dummy text of the printing and typesetting industry</li>
    <li>Lorem Ipsum is simply dummy text of the printing and typesetting industry</li>
    <li>Lorem Ipsum is simply dummy text of the printing and typesetting industry</li>
  </ul>
  <div class="wordmark"><span class="dot"></span>Veyrant</div>
  <div class="bar bottom"></div>
</section>

<section class="sheet card card-back">
  <div class="bar top"></div>
  <div class="road-area" role="img" aria-label="Soft winding road graphic in lilac and sage"></div>
  <ul class="services">
    <li>Automating Chain of Responsibility</li>
    <li>Paperless QBRTE &amp; Velmorix</li>
    <li>Providing Eco-Driving &amp; KLAP Reporting</li>
    <li>Electronic Work Diaries, Safe Driving Plans</li>
  </ul>
  <div class="wordmark"><span class="dot"></span>Veyrant</div>
  <div class="bar bottom"></div>
</section>

<section class="sheet card card-front">
  <div class="wordmark"><span class="dot"></span>Veyrant</div>
  <div class="contact">
    <p class="name">Marisol Reyes</p>
    <p>Director</p>
    <p>M 0400 123 456</p>
    <p>E marisol@veyrant.com</p>
  </div>
  <p class="web">veyrant.com</p>
  <div class="bar bottom"></div>
</section>
</body>
</html>
```